Advertising material for new program

We are launching a new program and need some advertising material.
- Cover photo for facebook (with minimal words on it)
- Social Media graphic (with minimal words on it)
- a5 flyer
- Banner

Information:
- Sensory play is a NEW program at Wren Tumblehall
What is Sensory Play:
*A sensory experience for babies 0 - 13months old.
* Stimulating babies senses
* Engaging movement and balance
- Created by qualified early childhood professional
- starting on Wednesdays in February 2022
- Book online
*www.wrentumblehall.example
-Contact us for more information
*97316258
*info@wrentumblehall.example

NOT INFORMATION FOR THE ADVERTISING
I have attached our style guide, our logo, some material we have done done recently and some photo of my own baby. As its a new program we don't have any photos yet but I am open to ideas

Target Market(s)

Mums aged 25 - 45

Industry/Entity Type

Kids activities

Colors
0054AA
0677BA
7BADD7
CADEEF
E8F1F8
59FF00
82FF00
B8FF75
E3FFCB
F4FFEA

Requirements
Must have
• photos of babies and mums with babies
Should not have
• Photos of adults / teens

```html
<!DOCTYPE html>
<html lang="en">
<head>
<meta charset="utf-8">
<title>Sensory Play – Wren Tumblehall</title>
<link rel="stylesheet" href="https://fonts.googleapis.com/css2?family=Montserrat:wght@400;500;600;700;800&display=swap">
<style>
  :root {
    --board-green: #99c900;
    --lime: #a2da00;
    --navy: #0b2a5c;
    --white: #ffffff;
    --photo-light: #eef0f2;
    --photo-warm: #f1d6c4;
    --photo-cool: #c9d3dc;
  }
  * { box-sizing: border-box; margin: 0; padding: 0; }
  html, body { width: 1200px; height: 1200px; overflow: hidden; }
  body {
    background: var(--board-green);
    font-family: "Montserrat", sans-serif;
    color: var(--navy);
    position: relative;
  }
  .board-title {
    position: absolute; left: 0; width: 1200px; top: 100px;
    text-align: center; font-weight: 800; font-size: 31px; letter-spacing: 0.5px;
    color: var(--navy);
  }
  .piece {
    position: absolute; background: var(--white); overflow: hidden;
    transform-origin: 0 0; transform: scale(0.6211);
    box-shadow: 0 24px 48px rgba(0, 40, 0, 0.35);
  }
  .piece--flyer { left: 26px; top: 194px; width: 868px; height: 1233px; }
  .piece--square { left: 587px; top: 337px; width: 919px; height: 919px; }
  .piece > * { position: absolute; }
  .swoosh { left: 0; top: 0; width: 100%; height: 100%; }
  .brand-name {
    font-weight: 800; color: var(--navy); text-align: center; line-height: 1.05;
    letter-spacing: 0.5px; white-space: nowrap;
  }
  .hero-photo {
    border-radius: 50%;
    background: radial-gradient(circle at 55% 35%, var(--photo-warm) 0 22%, var(--photo-light) 45%, var(--photo-cool) 100%);
  }
  .corner-photo {
    background: linear-gradient(160deg, rgba(241, 214, 196, 0.95), rgba(238, 240, 242, 0.9) 60%, rgba(200, 205, 212, 0.85));
    border-radius: 46% 40% 0 0;
  }
  .headline { font-weight: 800; line-height: 0.93; letter-spacing: -1px; }
  .intro-bar {
    background: var(--lime); font-weight: 500; text-align: center; white-space: nowrap;
    display: flex; align-items: center; justify-content: center;
  }
  .features { list-style: none; }
  .features li { display: flex; align-items: center; gap: 16px; font-weight: 700; font-size: 19px; letter-spacing: 0.3px; white-space: nowrap; }
  .features svg { width: 38px; height: 38px; flex: none; }
  .credentials { font-weight: 500; font-size: 22px; letter-spacing: 0.4px; white-space: nowrap; }
  .start-box { background: var(--lime); font-weight: 800; text-align: center; line-height: 1; white-space: nowrap; }
  .booking { text-align: center; line-height: 1.15; white-space: nowrap; }
  .booking .label { font-weight: 400; }
  .booking .url { font-weight: 500; }
  .contact { color: var(--lime); white-space: nowrap; }
  .contact .label { font-weight: 400; letter-spacing: 0.5px; }
  .contact .lines { display: flex; align-items: center; gap: 22px; font-weight: 600; margin-top: 14px; }
  .contact .lines span { display: inline-flex; align-items: center; gap: 6px; }
  .contact svg { fill: var(--white); }
</style>
</head>
<body>
<svg width="0" height="0" style="position:absolute">
  <defs>
    <symbol id="tick" viewBox="0 0 38 38">
      <circle cx="19" cy="19" r="18" fill="#8cc63f"/>
      <path d="M10 19.5 L16.5 26 L28 12.5" fill="none" stroke="#fff" stroke-width="3.6" stroke-linecap="round" stroke-linejoin="round"/>
    </symbol>
  </defs>
</svg>

<div class="board-title">OPTION 2</div>

<!-- A5 flyer -->
<section class="piece piece--flyer">
  <svg class="swoosh" viewBox="0 0 868 1233" preserveAspectRatio="none">
    <path d="M0 0 H868 V350 C600 352 250 322 0 218 Z" fill="#0b2a5c"/>
    <path d="M70 0 H868 V338 C560 332 240 232 70 0 Z" fill="#ffffff"/>
    <path d="M96 0 H868 V330 C560 322 262 222 96 0 Z" fill="#a2da00"/>
    <path d="M0 1060 C300 1125 600 1085 868 1020 V1233 H0 Z" fill="#a2da00"/>
    <path d="M0 1092 C300 1135 600 1102 868 1046 V1233 H0 Z" fill="#0b2a5c"/>
  </svg>
  <div class="hero-photo" role="img" aria-label="Photo of a baby on its tummy reaching for a colourful ball toy" style="left:395px; top:32px; width:456px; height:456px;"></div>
  <div class="brand-name" style="left:160px; top:48px; width:260px; font-size:32px;">WREN<br>TUMBLEHALL</div>
  <h1 class="headline" style="left:38px; top:350px; font-size:84px;">SENSORY<br>PLAY</h1>
  <div class="intro-bar" style="left:68px; top:519px; width:734px; height:40px; font-size:22px;">SENSORY PLAY IS A NEW PROGRAM AT WREN TUMBLEHALL</div>
  <ul class="features" style="left:128px; top:606px;">
    <li style="height:52px;"><svg><use href="#tick"/></svg>A SENSORY EXPERIENCE FOR BABIES 0 - 13MONTHS OLD</li>
    <li style="height:52px;"><svg><use href="#tick"/></svg>STIMULATING BABIES SENSES</li>
    <li style="height:52px;"><svg><use href="#tick"/></svg>ENGAGING MOVEMENT AND BALANCE</li>
  </ul>
  <p class="credentials" style="left:78px; top:806px;">CREATED BY QUALIFIED EARLY CHILDHOOD PROFESSIONAL</p>
  <div class="start-box" style="left:77px; top:895px; width:472px; height:92px; padding-top:10px;">
    <div style="font-size:30px;">STARTING ON WEDNESDAYS</div>
    <div style="font-size:46px; margin-top:2px;">IN FEBRUARY 2022</div>
  </div>
  <div class="booking" style="left:100px; top:1015px; width:380px;">
    <div class="label" style="font-size:21px;">BOOK ONLINE</div>
    <div class="url" style="font-size:20px;">WWW.WRENTUMBLEHALL.EXAMPLE</div>
  </div>
  <div class="corner-photo" role="img" aria-label="Photo of a smiling baby crawling" style="left:605px; top:912px; width:263px; height:321px;"></div>
  <div class="contact" style="left:97px; top:1150px;">
    <div class="label" style="font-size:21px;">CONTACT US FOR MORE INFORMATION</div>
    <div class="lines" style="font-size:16px;">
      <span><svg width="16" height="18" viewBox="0 0 16 18"><path d="M4 1 L6.5 5 L4.8 7 C5.8 9.5 7.5 11.5 9.5 12.8 L11.5 11 L15 13.8 L13 17 C6 16 1.5 9.5 1 3 Z"/></svg>97316258</span>
      <span><svg width="24" height="16" viewBox="0 0 24 16"><path d="M1 1 H23 V15 H1 Z M2.5 2.5 L12 9.5 L21.5 2.5 Z" fill-rule="evenodd"/></svg>INFO@WRENTUMBLEHALL.EXAMPLE</span>
    </div>
  </div>
</section>

<!-- Social media square -->
<section class="piece piece--square">
  <svg class="swoosh" viewBox="0 0 919 919" preserveAspectRatio="none">
    <path d="M0 0 H919 V195 C620 205 300 160 0 55 Z" fill="#0b2a5c"/>
    <path d="M160 0 H919 V185 C640 190 360 130 160 0 Z" fill="#ffffff"/>
    <path d="M188 0 H919 V178 C640 182 380 122 188 0 Z" fill="#a2da00"/>
    <path d="M0 740 C300 820 600 795 919 735 V919 H0 Z" fill="#a2da00"/>
    <path d="M0 768 C300 830 600 812 919 755 V919 H0 Z" fill="#0b2a5c"/>
  </svg>
  <div class="hero-photo" role="img" aria-label="Photo of a baby on its tummy reaching for a colourful ball toy" style="left:555px; top:8px; width:340px; height:340px;"></div>
  <div class="brand-name" style="left:355px; top:32px; width:190px; font-size:25px;">WREN<br>TUMBLEHALL</div>
  <h1 class="headline" style="left:68px; top:198px; font-size:84px;">SENSORY<br>PLAY</h1>
  <div class="intro-bar" style="left:143px; top:363px; width:666px; height:36px; font-size:19px;">SENSORY PLAY IS A NEW PROGRAM AT WREN TUMBLEHALL</div>
  <ul class="features" style="left:160px; top:428px;">
    <li style="height:54px;"><svg><use href="#tick"/></svg>A SENSORY EXPERIENCE FOR BABIES 0 - 13MONTHS OLD</li>
    <li style="height:54px;"><svg><use href="#tick"/></svg>STIMULATING BABIES SENSES</li>
    <li style="height:54px;"><svg><use href="#tick"/></svg>ENGAGING MOVEMENT AND BALANCE</li>
  </ul>
  <p class="credentials" style="left:140px; top:626px;">CREATED BY QUALIFIED EARLY CHILDHOOD PROFESSIONAL</p>
  <div class="start-box" style="left:139px; top:674px; width:327px; height:60px; padding-top:5px;">
    <div style="font-size:19px;">STARTING ON WEDNESDAYS</div>
    <div style="font-size:29px;">IN FEBRUARY 2022</div>
  </div>
  <div class="booking" style="left:120px; top:744px; width:350px;">
    <div class="label" style="font-size:18px;">BOOK ONLINE</div>
    <div class="url" style="font-size:17px;">WWW.WRENTUMBLEHALL.EXAMPLE</div>
  </div>
  <div class="corner-photo" role="img" aria-label="Photo of a smiling baby crawling" style="left:690px; top:672px; width:229px; height:247px;"></div>
  <div class="contact" style="left:123px; top:840px;">
    <div class="label" style="font-size:19px;">CONTACT US FOR MORE INFORMATION</div>
    <div class="lines" style="font-size:15px; margin-top:12px;">
      <span><svg width="15" height="17" viewBox="0 0 16 18"><path d="M4 1 L6.5 5 L4.8 7 C5.8 9.5 7.5 11.5 9.5 12.8 L11.5 11 L15 13.8 L13 17 C6 16 1.5 9.5 1 3 Z"/></svg>97316258</span>
      <span><svg width="22" height="15" viewBox="0 0 24 16"><path d="M1 1 H23 V15 H1 Z M2.5 2.5 L12 9.5 L21.5 2.5 Z" fill-rule="evenodd"/></svg>INFO@WRENTUMBLEHALL.EXAMPLE</span>
    </div>
  </div>
</section>
</body>
</html>
```